Wordpress Design Project (Darvy)

We need a wordpress design for an established auction and real estate company based in Pennsylvania. The winning design will incorporate a professional layout with and company logo in a very simple and clean layout.

Industry/Entity Type

Real Estate

Requirements
Must have
• Navigation:
1) Home; 2) Auctions; 3) Appraisals; 4) Real Estate; 5) FAQ; 6) About Us; 7) Contact Us.

Site will have overall layout of https://www.plumvesta.com/featured/regions/the-northeast. Home page will have logo and navigation at top. The navigation bar will also have social media icons (facebook, Google+, RSS, twitter) inside it. There will be text in the content area - use lorem ipsum. The image attached will be used below text (auctions.jpg) . Footer will have smaller company loogo, the attached affiliation logos and social media icons.

Logo attached. Color scheme will be black, gray, and red as accent color.
Nice to have
• navigation will have dropdowns, nice to have one represented - under auctions 'All Auctions' will be dropdown.

```html
<!DOCTYPE html>
<html lang="en">
<head>
<meta charset="utf-8">
<title>Darvy Auctioneers &amp; Appraisers</title>
<link href="https://fonts.googleapis.com/css2?family=Noto+Serif:wght@400;700&display=swap" rel="stylesheet">
<style>
  :root {
    --red: #d62027;
    --dark: #1a1a1a;
    --text: #222;
    --grey-bg: #f4f4f4;
    --footer-bg: #e9e9e9;
    --line: #cfcfcf;
    --white: #fff;
  }
  * { box-sizing: border-box; margin: 0; padding: 0; }
  html, body { width: 722px; height: 1200px; overflow: hidden; }
  body {
    position: relative;
    font-family: "Noto Serif", Georgia, serif;
    color: var(--text);
    background: var(--grey-bg);
  }
  .site-header {
    position: absolute; left: 0; top: 0; width: 722px; height: 65px;
    background: var(--white); border-bottom: 1px solid var(--line);
    box-shadow: 0 1px 3px rgba(0,0,0,.12);
  }
  .brand {
    position: absolute; left: 76px; top: 11px;
    display: flex; align-items: center; gap: 6px;
    font-size: 28px; font-weight: 700; color: var(--dark); line-height: 1;
  }
  .brand-square { width: 42px; height: 42px; background: var(--red); border-radius: 3px; }
  .social { position: absolute; display: flex; gap: 5px; }
  .social span { width: 17px; height: 17px; display: block; border-radius: 2px; background: var(--dark); }
  .social span:first-child { background: var(--red); }
  .header-social { left: 566px; top: 12px; }
  .main-nav {
    position: absolute; right: 75px; top: 38px;
    display: flex; gap: 12px; font-size: 10px;
  }
  .main-nav a { color: var(--dark); text-decoration: none; padding: 1px 5px; }
  .main-nav a.current { color: var(--red); border: 1px solid var(--red); border-radius: 2px; border-top-width: 2px; }
  .hero {
    position: absolute; left: 76px; top: 64px; width: 571px; height: 256px;
    border: 3px solid var(--red); border-top: none;
    background: linear-gradient(180deg, #2a3a8a 0%, #1d2a6e 55%, #3a3540 100%);
    box-shadow: 0 12px 10px -8px rgba(0,0,0,.35);
  }
  .hero-arrow {
    position: absolute; top: 175px; width: 24px; height: 26px;
    background: var(--red); display: flex; align-items: center; justify-content: center;
  }
  .hero-arrow.prev { left: 63px; border-radius: 13px 0 0 13px; }
  .hero-arrow.next { left: 637px; border-radius: 0 13px 13px 0; }
  .listings {
    position: absolute; left: 77px; top: 342px;
    display: grid; grid-template-columns: 270px 270px; column-gap: 28px;
    grid-auto-rows: 253.5px;
  }
  .listing { text-align: center; }
  .listing-photo {
    height: 172px; border: 4px solid var(--white); outline: 1px solid #d4d4d4;
    box-shadow: 0 8px 8px -6px rgba(0,0,0,.35);
  }
  .photo-wood { background: linear-gradient(135deg, #a97e5c, #6b4a33); }
  .photo-wood.pale { background: linear-gradient(135deg, #d8c4b4, #b49684); }
  .photo-counter { background: linear-gradient(180deg, #d9cbb8 0%, #2f2b2a 40%, #b37a43 75%, #8a5a2e 100%); }
  .photo-rugs { background: linear-gradient(135deg, #8a8276, #b9b8b2 50%, #7f8b93); }
  .photo-doors { background: linear-gradient(90deg, #d6dde4, #f1f3f5 50%, #b89a5c); }
  .listing-title { margin-top: 7px; font-size: 15px; font-weight: 400; color: var(--red); letter-spacing: .3px; }
  .listing-text { margin-top: 3px; font-size: 8.6px; line-height: 13px; padding: 0 2px; }
  .listing-meta {
    margin-top: 8px; font-size: 8.6px; display: flex; justify-content: center; align-items: center; gap: 4px;
  }
  .listing-meta svg { display: block; }
  .listing-meta .gap { width: 6px; }
  .site-footer {
    position: absolute; left: 0; top: 1109px; width: 722px; height: 91px;
    background: var(--footer-bg); border-top: 1px solid var(--line);
  }
  .footer-nav {
    position: absolute; left: 76px; top: 10px;
    display: grid; grid-template-columns: 77px 60px; grid-auto-rows: 19px; grid-auto-flow: column;
    grid-template-rows: repeat(4, 19px); font-size: 7.5px;
  }
  .footer-nav a { color: var(--dark); text-decoration: none; }
  .footer-nav a.current { color: var(--red); }
  .badges {
    position: absolute; left: 290px; top: 12px;
    display: grid; grid-template-columns: repeat(3, 32px); column-gap: 26px; row-gap: 12px;
  }
  .badge { width: 32px; height: 30px; background: #9a9a9a; }
  .badge.round { border-radius: 50%; background: #b3b3b3; }
  .footer-social { left: 538px; top: 12px; }
  .footer-brand {
    position: absolute; left: 538px; top: 38px;
    display: flex; align-items: center; gap: 5px;
    font-size: 20px; font-weight: 700; color: var(--dark); line-height: 1;
  }
  .footer-brand .brand-square { width: 28px; height: 28px; }
  .copyright { position: absolute; left: 538px; top: 75px; font-size: 7.5px; color: var(--dark); }
</style>
</head>
<body>
<header class="site-header">
  <div class="brand"><span class="brand-square"></span>Darvy</div>
  <div class="social header-social"><span></span><span></span><span></span><span></span></div>
  <nav class="main-nav">
    <a class="current" href="#">Home</a><a href="#">Auctions</a><a href="#">Appraisals</a><a href="#">Real Estate</a><a href="#">FAQ</a><a href="#">About Us</a><a href="#">Contact Us</a>
  </nav>
</header>

<div class="hero" role="img" aria-label="Auctioneer at a podium addressing a sale room, with staff seated at tables and a screen showing the current lot"></div>
<div class="hero-arrow prev"><svg width="8" height="8" viewBox="0 0 8 8"><path d="M6 0 L1 4 L6 8Z" fill="#fff"/></svg></div>
<div class="hero-arrow next"><svg width="8" height="8" viewBox="0 0 8 8"><path d="M2 0 L7 4 L2 8Z" fill="#fff"/></svg></div>

<main class="listings">
  <article class="listing">
    <div class="listing-photo photo-wood pale" role="img" aria-label="Wooden cabinets and cupboards tagged for auction"></div>
    <h2 class="listing-title">Lorem ipsum dolor sit amet</h2>
    <p class="listing-text">Lorem ipsum dolor sit amet, consectetur adipiscing elit. Integer facilisis feugiat diam, quis vehicula enim fringilla nec</p>
    <div class="listing-meta"><svg width="13" height="13" viewBox="0 0 13 13"><circle cx="6.5" cy="7" r="5" fill="none" stroke="#d62027" stroke-width="1.6"/><path d="M6.5 4.5V7H8.5" stroke="#d62027" stroke-width="1.3" fill="none"/></svg>12 : 30 AM<span class="gap"></span><svg width="13" height="13" viewBox="0 0 13 13"><rect x="1" y="2" width="11" height="10" fill="none" stroke="#d62027" stroke-width="1.5"/><rect x="1" y="2" width="11" height="3" fill="#d62027"/></svg>Thusday 15 / 08 / 2013</div>
  </article>
  <article class="listing">
    <div class="listing-photo photo-counter" role="img" aria-label="Vanity unit with granite top and sink"></div>
    <h2 class="listing-title">Lorem ipsum dolor sit amet</h2>
    <p class="listing-text">Lorem ipsum dolor sit amet, consectetur adipiscing elit. Integer facilisis feugiat diam, quis vehicula enim fringilla nec</p>
    <div class="listing-meta"><svg width="13" height="13" viewBox="0 0 13 13"><circle cx="6.5" cy="7" r="5" fill="none" stroke="#d62027" stroke-width="1.6"/><path d="M6.5 4.5V7H8.5" stroke="#d62027" stroke-width="1.3" fill="none"/></svg>12 : 30 AM<span class="gap"></span><svg width="13" height="13" viewBox="0 0 13 13"><rect x="1" y="2" width="11" height="10" fill="none" stroke="#d62027" stroke-width="1.5"/><rect x="1" y="2" width="11" height="3" fill="#d62027"/></svg>Thusday 15 / 08 / 2013</div>
  </article>
  <article class="listing">
    <div class="listing-photo photo-rugs" role="img" aria-label="Rolled carpets with yellow lot tags"></div>
    <h2 class="listing-title">Lorem ipsum dolor sit amet</h2>
    <p class="listing-text">Lorem ipsum dolor sit amet, consectetur adipiscing elit. Integer facilisis feugiat diam, quis vehicula enim fringilla nec</p>
    <div class="listing-meta"><svg width="13" height="13" viewBox="0 0 13 13"><circle cx="6.5" cy="7" r="5" fill="none" stroke="#d62027" stroke-width="1.6"/><path d="M6.5 4.5V7H8.5" stroke="#d62027" stroke-width="1.3" fill="none"/></svg>12 : 30 AM<span class="gap"></span><svg width="13" height="13" viewBox="0 0 13 13"><rect x="1" y="2" width="11" height="10" fill="none" stroke="#d62027" stroke-width="1.5"/><rect x="1" y="2" width="11" height="3" fill="#d62027"/></svg>Thusday 15 / 08 / 2013</div>
  </article>
  <article class="listing">
    <div class="listing-photo photo-doors" role="img" aria-label="Row of white glazed doors"></div>
    <h2 class="listing-title">Lorem ipsum dolor sit amet</h2>
    <p class="listing-text">Lorem ipsum dolor sit amet, consectetur adipiscing elit. Integer facilisis feugiat diam, quis vehicula enim fringilla nec</p>
    <div class="listing-meta"><svg width="13" height="13" viewBox="0 0 13 13"><circle cx="6.5" cy="7" r="5" fill="none" stroke="#d62027" stroke-width="1.6"/><path d="M6.5 4.5V7H8.5" stroke="#d62027" stroke-width="1.3" fill="none"/></svg>12 : 30 AM<span class="gap"></span><svg width="13" height="13" viewBox="0 0 13 13"><rect x="1" y="2" width="11" height="10" fill="none" stroke="#d62027" stroke-width="1.5"/><rect x="1" y="2" width="11" height="3" fill="#d62027"/></svg>Thusday 15 / 08 / 2013</div>
  </article>
  <article class="listing">
    <div class="listing-photo photo-rugs" role="img" aria-label="Rolled carpets with yellow lot tags"></div>
    <h2 class="listing-title">Lorem ipsum dolor sit amet</h2>
    <p class="listing-text">Lorem ipsum dolor sit amet, consectetur adipiscing elit. Integer facilisis feugiat diam, quis vehicula enim fringilla nec</p>
    <div class="listing-meta"><svg width="13" height="13" viewBox="0 0 13 13"><circle cx="6.5" cy="7" r="5" fill="none" stroke="#d62027" stroke-width="1.6"/><path d="M6.5 4.5V7H8.5" stroke="#d62027" stroke-width="1.3" fill="none"/></svg>12 : 30 AM<span class="gap"></span><svg width="13" height="13" viewBox="0 0 13 13"><rect x="1" y="2" width="11" height="10" fill="none" stroke="#d62027" stroke-width="1.5"/><rect x="1" y="2" width="11" height="3" fill="#d62027"/></svg>Thusday 15 / 08 / 2013</div>
  </article>
  <article class="listing">
    <div class="listing-photo photo-doors" role="img" aria-label="Row of white glazed doors"></div>
    <h2 class="listing-title">Lorem ipsum dolor sit amet</h2>
    <p class="listing-text">Lorem ipsum dolor sit amet, consectetur adipiscing elit. Integer facilisis feugiat diam, quis vehicula enim fringilla nec</p>
    <div class="listing-meta"><svg width="13" height="13" viewBox="0 0 13 13"><circle cx="6.5" cy="7" r="5" fill="none" stroke="#d62027" stroke-width="1.6"/><path d="M6.5 4.5V7H8.5" stroke="#d62027" stroke-width="1.3" fill="none"/></svg>12 : 30 AM<span class="gap"></span><svg width="13" height="13" viewBox="0 0 13 13"><rect x="1" y="2" width="11" height="10" fill="none" stroke="#d62027" stroke-width="1.5"/><rect x="1" y="2" width="11" height="3" fill="#d62027"/></svg>Thusday 15 / 08 / 2013</div>
  </article>
</main>

<footer class="site-footer">
  <nav class="footer-nav">
    <a class="current" href="#">Home</a><a href="#">Auctions</a><a href="#">Appraisals</a><a href="#">Real Estate</a>
    <a href="#">FAQ</a><a href="#">About Us</a><a href="#">Contact Us</a><a href="#">Sitemap</a>
  </nav>
  <div class="badges">
    <span class="badge"></span><span class="badge round"></span><span class="badge round"></span>
    <span class="badge"></span><span class="badge"></span><span class="badge round"></span>
  </div>
  <div class="social footer-social"><span></span><span></span><span></span><span></span></div>
  <div class="footer-brand"><span class="brand-square"></span>Darvy</div>
  <p class="copyright">Copyright © 2013 Darvy</p>
</footer>
</body>
</html>
```